New Business Card Design Project

I would like to purchase a customized version of a design you have previously submitted - https://www.artmarketly.com/design/5184926<br/><br/>I need a design for a swimming pool business card. The services we provide are Maintenance, Repairs and Installations so if you include that in the card. I would also like my email bluecrestpoolsservice@mailora.com, my address 48631 Corvell Dr. Fenwick Hollow ZZ, phone number 555-555-0173. Id like to have the two o's in Bluecrest Pools look like an actual pool.

```html
<!DOCTYPE html>
<html lang="en">
<head>
<meta charset="utf-8">
<title>Bluecrest Pools — Business Card</title>
<link href="https://fonts.googleapis.com/css2?family=Quicksand:wght@400;500;700&display=swap" rel="stylesheet">
<style>
  :root {
    --backdrop: #d3d3d3;
    --card: #26292c;
    --card-edge: #2e3236;
    --brand-blue: #29abe2;
    --text-light: #e9ecee;
    --text-muted: #c9cdd0;
    --name-silver: #c7cbce;
    --rule: #8a8f93;
  }
  * { margin: 0; padding: 0; box-sizing: border-box; }
  html, body {
    width: 1200px; height: 1042px; overflow: hidden;
    background: var(--backdrop);
    font-family: "Quicksand", sans-serif;
  }
  .canvas { position: relative; width: 1200px; height: 1042px; }
  .card {
    position: absolute;
    width: 560px; height: 320px;
    background: linear-gradient(160deg, var(--card-edge), var(--card));
    border-radius: 4px;
    box-shadow: 0 12px 30px rgba(0,0,0,.18);
    color: var(--text-light);
  }
  .card--front { left: 560px; top: 150px; padding: 40px 44px; }
  .card--back { left: 110px; top: 560px; display: flex; align-items: center; justify-content: center; }

  .brand-name {
    font-weight: 700; font-size: 60px; letter-spacing: -1px;
    color: var(--brand-blue); line-height: 1;
  }
  .card--back .brand-name { color: var(--name-silver); font-size: 50px; }

  .tagline {
    margin-top: 12px; font-weight: 500; font-size: 19px;
    color: var(--text-light); letter-spacing: .3px;
  }
  .tagline .dot { color: var(--brand-blue); }

  .divider { margin: 24px 0 24px; height: 1px; background: var(--rule); }

  .contacts { display: grid; grid-template-columns: auto 1fr; gap: 18px 30px; font-size: 16px; color: var(--text-muted); }
  .contact { display: flex; align-items: center; gap: 8px; white-space: nowrap; }
  .contact svg { width: 16px; height: 16px; fill: var(--brand-blue); flex: none; }
  .contact--address { grid-column: 1 / span 2; }
</style>
</head>
<body>
<main class="canvas">
  <section class="card card--front" aria-label="Business card front">
    <h1 class="brand-name">Bluecrest Pools</h1>
    <p class="tagline"><span class="dot">.</span> Maintenance, Repairs &amp; Installations <span class="dot">.</span></p>
    <div class="divider"></div>
    <div class="contacts">
      <span class="contact contact--phone">
        <svg viewBox="0 0 24 24" aria-hidden="true"><path d="M6.6 10.8a15.1 15.1 0 0 0 6.6 6.6l2.2-2.2a1 1 0 0 1 1-.25 11.4 11.4 0 0 0 3.6.57 1 1 0 0 1 1 1V20a1 1 0 0 1-1 1A17 17 0 0 1 3 4a1 1 0 0 1 1-1h3.5a1 1 0 0 1 1 1c0 1.25.2 2.45.57 3.57a1 1 0 0 1-.25 1z"/></svg>
        555-555-0173
      </span>
      <span class="contact contact--email">
        <svg viewBox="0 0 24 24" aria-hidden="true"><path d="M2 5h20v14H2zm2 2v.5l8 5 8-5V7zm0 2.8V17h16V9.8l-8 5z"/></svg>
        bluecrestpoolsservice@mailora.com
      </span>
      <span class="contact contact--address">
        <svg viewBox="0 0 24 24" aria-hidden="true"><path d="M12 3 2 12h3v8h5v-5h4v5h5v-8h3z"/></svg>
        48631 Corvell Dr. Fenwick Hollow ZZ,
      </span>
    </div>
  </section>

  <section class="card card--back" aria-label="Business card back">
    <p class="brand-name">Bluecrest Pools</p>
  </section>
</main>
</body>
</html>
```